Webdesign für Rheinau Vita Forschungsbund e.V.
Zielgruppe
Vereinsmitglieder aus der Bio-Tech-Branche, Öffentlichkeit
Aufgabenstellung
Wir benötigen ein Webdesign für die Website des Rheinau Vita Forschungsbund e.V., zu liefern als PSD-Datei.

```html
<!DOCTYPE html>
<html lang="de">
<head>
<meta charset="utf-8">
<title>Rheinau Vita Forschungsbund e.V.</title>
<link rel="stylesheet" href="https://fonts.googleapis.com/css2?family=Ubuntu:wght@400;500;700&display=swap">
<style>
:root{
  --petrol:#17709c;
  --petrol-dark:#0f5a80;
  --mint:#4cc3b5;
  --mint-line:#7fd6cc;
  --ink:#1c1c1c;
  --grey-line:#9a9a9a;
  --page:#ffffff;
  --haze:#e9eef6;
}
*{margin:0;padding:0;box-sizing:border-box}
html,body{width:1200px;height:938px;overflow:hidden;background:var(--page)}
body{font-family:"Ubuntu",sans-serif;color:var(--ink);position:relative}
.backdrop{position:absolute;left:0;top:150px;width:1200px;height:788px;
  background:radial-gradient(ellipse at 50% 30%,#e3e9f3 0%,#eef2f8 45%,#fbfcfe 80%)}
.hero{position:absolute;left:363px;top:12px;width:798px;height:161px;
  border-radius:160px 12px 0 0/161px 12px 0 0;
  background:linear-gradient(90deg,#e6ebf4 0%,#c9d3e6 35%,#bac7e0 60%,#aebfe0 100%);
  box-shadow:0 10px 14px -8px rgba(60,70,90,.35)}
.logo{position:absolute;left:41px;top:40px;display:flex;flex-direction:column;align-items:center;gap:14px}
.logo-dot{width:50px;height:50px;border-radius:50%;background:var(--mint);margin-left:-40px}
.logo-name{font-size:14px;font-weight:500;letter-spacing:1.6px;color:#333}
.meta-nav{position:absolute;left:981px;top:25px;font-size:14px;font-weight:500;color:var(--petrol)}
.meta-nav span{margin:0 14px}
.main-nav{position:absolute;left:39px;top:235px;width:126px;list-style:none}
.main-nav li{border-top:1px solid var(--grey-line);height:37.5px;line-height:37px;padding-left:15px;font-size:16px;color:#333}
.main-nav li:last-child{border-bottom:1px solid var(--grey-line)}
.intro{position:absolute;left:246px;top:286px;width:580px;font-size:16.3px;line-height:19.5px;color:var(--petrol)}
.intro strong{font-size:19px;font-weight:500}
.intro p+p{margin-top:19px}
.card{position:absolute;background:#fff;border:1px solid var(--mint-line);border-radius:12px;
  box-shadow:0 12px 14px -10px rgba(60,70,90,.4)}
.news{left:39px;top:519px;width:764px;height:349px;padding:10px 11px}
.card-title{font-size:16px;font-weight:500;color:var(--petrol);text-transform:uppercase}
.news-item{margin-top:19px}
.news-item+.news-item{margin-top:7px}
.news-head{font-size:16px;font-weight:500;color:var(--mint);text-decoration:underline}
.news-text{margin-top:7px;font-size:13.5px;line-height:17px;width:730px}
.more{display:block;text-align:right;font-size:10px;font-weight:500;color:var(--mint);text-decoration:underline;margin-top:11px;padding-right:44px}
.events{left:890px;top:122px;width:264px;height:746px;padding:20px 16px}
.events .card-title{border-bottom:2px dotted #999;padding-bottom:6px}
.event{position:relative;padding-left:25px;margin-top:22px;height:138px}
.event+.event{margin-top:22px}
.event::before{content:"";position:absolute;left:3px;top:18px;width:8px;height:8px;border-radius:50%;background:var(--petrol)}
.event-date{font-size:10.5px;font-weight:500}
.event-name{margin-top:7px;font-size:15.5px;font-weight:500;color:var(--mint)}
.event-text{margin-top:8px;font-size:10.5px;line-height:14px}
.event .more{text-align:left;padding:0;margin-top:17px}
.deco-cells{position:absolute;left:1060px;top:740px;width:140px;height:198px;
  background:radial-gradient(circle at 70% 60%,#6fc4d2 0%,rgba(111,196,210,.5) 45%,rgba(255,255,255,0) 72%)}
.foot-nav{position:absolute;left:48px;top:913px;font-size:10px;color:#333;display:flex;gap:21px}
</style>
</head>
<body>
<div class="backdrop" role="img" aria-label="Blasses Laborfoto mit Glasbehältern als Seitenhintergrund"></div>
<div class="hero" role="img" aria-label="Foto von Laborfläschchen mit dunklen Schraubdeckeln und blauer Flüssigkeit"></div>
<div class="deco-cells" role="img" aria-label="Dekorative Zellstruktur in Türkis"></div>

<div class="logo">
  <div class="logo-dot"></div>
  <div class="logo-name">RHEINAU VITA FORSCHUNGSBUND</div>
</div>

<nav class="meta-nav">Start<span>I</span>Impressum</nav>

<ul class="main-nav">
  <li>Über Uns</li><li>Veranstaltungen</li><li>Aktuelles</li><li>Region</li><li>Service</li><li>Kontakt</li>
</ul>

<div class="intro">
  <p>Die <strong>Rheinau Vita Forschungsbund</strong> versteht sich als Schrittmacher für die Biotechnologie-Region Rhein-Main. Wir sind qualifizierter Ansprechpartner für Unternehmen, Politik und Medien und Interessenvertretung für alle, die in der Wertschöpfungskette von der Grundlagenforschung bis zum fertigen Produkt und seiner Vermarktung arbeiten.</p>
  <p>Hierfür bieten wir ein in der Region einzigartiges Netzwerk.</p>
</div>

<section class="card news">
  <h2 class="card-title">Aktuelles</h2>
  <article class="news-item">
    <h3 class="news-head">Neue Spezies entdeckt</h3>
    <p class="news-text">Lorem ipsum dolor sit amet, consectetur adipiscing elit. Nullam elementum varius luctus. Nulla scelerisque sapien sit amet augue. orem ipsum dolor sit amet, con</p>
    <a class="more">mehr Informationen</a>
  </article>
  <article class="news-item">
    <h3 class="news-head">Neue Spezies entdeckt</h3>
    <p class="news-text">Lorem ipsum dolor sit amet, consectetur adipiscing elit. Nullam elementum varius luctus. Nulla scelerisque sapien sit amet augue. orem ipsum dolor sit amet, con</p>
    <a class="more">mehr Informationen</a>
  </article>
  <article class="news-item">
    <h3 class="news-head">Neue Spezies entdeckt</h3>
    <p class="news-text">Lorem ipsum dolor sit amet, consectetur adipiscing elit. Nullam elementum varius luctus. Nulla scelerisque sapien sit amet augue. orem ipsum dolor sit amet, con</p>
    <a class="more">mehr Informationen</a>
  </article>
</section>

<aside class="card events">
  <h2 class="card-title">Veranstaltungen</h2>
  <div class="event">
    <div class="event-date">07.12.10</div>
    <div class="event-name">Microtechnik</div>
    <p class="event-text">Hier steht eine kurze Beschreibung zum Thema und dann ein Link zum aufrufen der Veranstaltung</p>
    <a class="more">mehr Informationen</a>
  </div>
  <div class="event">
    <div class="event-date">09.12.10</div>
    <div class="event-name">Zellenaufbau</div>
    <p class="event-text">Hier steht eine kurze Beschreibung zum Thema und dann ein Link zum aufrufen der Veranstaltung</p>
    <a class="more">mehr Informationen</a>
  </div>
  <div class="event">
    <div class="event-date">18.12.10</div>
    <div class="event-name">Entwicklung des Nucleus</div>
    <p class="event-text">Hier steht eine kurze Beschreibung zum Thema und dann ein Link zum aufrufen der Veranstaltung</p>
    <a class="more">mehr Informationen</a>
  </div>
  <div class="event">
    <div class="event-date">20.12.10</div>
    <div class="event-name">Escherichia Coli</div>
    <p class="event-text">Hier steht eine kurze Beschreibung zum Thema und dann ein Link zum aufrufen der Veranstaltung</p>
    <a class="more">mehr Informationen</a>
  </div>
</aside>

<footer class="foot-nav">
  <span>Über Uns</span><span>Veranstaltungen</span><span>Aktuelles</span><span>Region</span><span>Service</span>
</footer>
</body>
</html>
```